Website for Excavator and Earthworks Company

We require a modern, sleek and practical website for our newly created earthworks/excavator business in Perth, Western Australia called Gullwind Stonecut Earthworks.

The website should have a modern, cutting edge feel but only needs to be relatively simplistic in it's layout and eventual functionality.

Some pages it should have would be Home, About, Projects and Contact Us.

Number of Pages Required

1 page

```html
<!DOCTYPE html>
<html lang="en">
<head>
<meta charset="utf-8">
<title>Gullwind Stonecut Earthworks</title>
<link href="https://fonts.googleapis.com/css2?family=Michroma&family=Inter:wght@400;600;700&display=swap" rel="stylesheet">
<style>
:root{
  --lime:#c8dc00;
  --ink:#111111;
  --paper:#ffffff;
  --mist:#f3f3f3;
  --line:#d9d9d9;
  --muted:#6a6a6a;
  --night:#161616;
}
*{margin:0;padding:0;box-sizing:border-box}
html,body{width:1200px;height:1200px;overflow:hidden;background:var(--paper)}
.page{position:absolute;left:451.5px;top:0;width:477px;height:1932px;transform:scale(.6211);transform-origin:0 0;font-family:'Inter',sans-serif;color:var(--ink);background:var(--paper)}
.abs{position:absolute}
.display{font-family:'Michroma',sans-serif;text-transform:uppercase;letter-spacing:.02em}
.lime-text{color:var(--lime)}
.photo{position:absolute}
.band{position:absolute;left:0;width:477px}
.band--mist{background:var(--mist)}
.eyebrow{position:absolute;left:0;width:477px;text-align:center;font-family:'Michroma',sans-serif;font-size:3.2px;font-weight:700;letter-spacing:.05em}
.eyebrow span{display:inline-block;position:relative;padding:0 4px}
.eyebrow span::before,.eyebrow span::after{content:"";position:absolute;top:50%;width:26px;height:.6px;background:var(--lime)}
.eyebrow span::before{right:100%}
.eyebrow span::after{left:100%}
.heading{position:absolute;left:0;width:477px;text-align:center;font-family:'Michroma',sans-serif;font-size:12.5px;line-height:16px;text-transform:uppercase}
.btn{position:absolute;display:flex;align-items:center;justify-content:center;gap:3px;font-size:3.6px;font-weight:700;text-transform:uppercase;letter-spacing:.02em}
.btn--lime{background:var(--lime);color:var(--ink)}
.btn--dark{background:var(--ink);color:#fff}
.btn--light{background:#fff;color:var(--ink)}
.body-copy{position:absolute;font-size:4.4px;line-height:7px;color:var(--muted)}
/* nav */
.brand{position:absolute;display:flex;align-items:center;gap:3px;font-family:'Michroma',sans-serif;font-size:4.2px;line-height:4.6px;color:var(--ink);text-transform:uppercase}
.brand i{display:block;width:8px;height:8px;background:var(--lime)}
.nav{position:absolute;left:151px;top:11px;display:flex;gap:14px;font-size:3.6px;font-weight:600;text-transform:uppercase}
/* hero */
.hero-title{position:absolute;left:55px;font-family:'Michroma',sans-serif;font-size:16.5px;line-height:19px;padding:0 2px;text-transform:uppercase}
/* cards */
.service{position:absolute;top:583px;width:118px;height:143px;overflow:hidden}
.service h3{position:absolute;left:7px;top:94px;font-family:'Michroma',sans-serif;font-size:7.5px;line-height:10px;text-transform:uppercase;font-weight:400}
.service p{position:absolute;left:7px;top:120px;width:95px;font-size:3.5px;line-height:5.4px;color:#ddd}
.tag{position:absolute;width:89px;height:15px;border:1px solid #bdbdbd;display:flex;align-items:center;justify-content:center;font-family:'Michroma',sans-serif;font-size:3.6px;text-transform:uppercase;background:#fff}
.trust{position:absolute;top:1267px;width:87px;height:83px;background:#fff;border:1px solid #e6e6e6;text-align:center}
.trust svg{position:absolute;left:35px;top:13px}
.trust h4{position:absolute;left:0;width:100%;font-family:'Michroma',sans-serif;font-size:5.2px;line-height:7.5px;font-weight:400;text-transform:uppercase}
.trust p{position:absolute;left:8px;width:71px;font-size:3.5px;line-height:5.6px;color:var(--muted)}
.review{position:absolute;top:1487px;width:118px;height:89px;background:#fff;border:1px solid #e7e7e7;padding:8px}
.stars{color:var(--lime);font-size:5.5px;letter-spacing:1.2px;line-height:6px}
.review blockquote{margin-top:6px;font-size:4.3px;line-height:7.8px;color:#333}
.review .who{position:absolute;left:8px;top:68px;font-size:3.5px;line-height:4.6px;font-weight:700;text-transform:uppercase}
.review .who small{display:block;font-weight:400;text-transform:none;color:var(--muted)}
.review .rule{position:absolute;left:8px;right:8px;top:64px;height:.5px;background:#eee}
/* footer */
.footer{position:absolute;left:0;top:1745px;width:477px;height:187px;background:var(--night);color:#bbb}
.footer h5{position:absolute;font-size:4.6px;font-weight:600;color:var(--lime)}
.footer ul{position:absolute;list-style:none;font-size:3.3px;line-height:9.2px;color:#aaa}
.social{position:absolute;top:1883px;width:5px;height:5px;border-radius:50%;background:#ddd}
</style>
</head>
<body>
<div class="page">

  <!-- HERO -->
  <div class="photo" role="img" aria-label="Yellow mini excavator parked on a grassy yard with trees behind" style="left:0;top:0;width:477px;height:268px;background:linear-gradient(180deg,#ffffff 0%,#e8ece2 10%,#8f9a78 30%,#8a9256 55%,#7c8a44 80%,#5d6834 100%)"></div>
  <div class="photo" role="img" aria-label="Excavator body in yellow" style="left:160px;top:30px;width:260px;height:230px;background:radial-gradient(ellipse at 55% 55%,#d9c63a 0%,#b9a830 35%,rgba(120,120,60,0) 70%)"></div>

  <div class="brand" style="left:55px;top:9px"><i></i><span>Gullwind Stonecut<br>Earthworks</span></div>
  <nav class="nav"><span>Home</span><span>About Us</span><span>Services</span><span>Projects</span><span>Contact</span></nav>
  <div class="btn btn--lime" style="left:317px;top:7px;width:42px;height:13px">Get a Quote</div>
  <div class="btn btn--dark" style="left:366px;top:7px;width:57px;height:13px">
    <svg width="5" height="5" viewBox="0 0 10 10"><circle cx="5" cy="5" r="4.4" fill="none" stroke="#fff" stroke-width=".8"/><path d="M3.3 2.8l1 1-.5.7c.4.8 1 1.4 1.8 1.8l.7-.5 1 1-.7.8c-1.9-.3-3.3-1.7-3.6-3.6z" fill="#fff"/></svg>+61 400 555 018</div>

  <div class="abs display" style="left:62px;top:87px;font-size:3.4px;font-weight:700">Perth, Western Australia</div>
  <div class="hero-title" style="top:100px;background:#fff">Professional</div>
  <div class="hero-title" style="top:119px;background:var(--lime)">Earthworks &amp; Excavation</div>
  <p class="body-copy" style="left:55px;top:145px;width:175px;font-size:4.2px;line-height:7px;color:#2a2a2a">From site preparation to trenching and demolition, Gullwind Stonecut Earthworks delivers reliable excavation services across the Perth metropolitan area with precision, powered by experience.</p>
  <div class="btn btn--lime" style="left:55px;top:176px;width:63px;height:14px">Request a Quote <span>↗</span></div>
  <div class="btn btn--light" style="left:123px;top:176px;width:54px;height:14px">View Our Works</div>

  <!-- ABOUT -->
  <div class="band band--mist" style="top:268px;height:229px"></div>
  <div class="photo" role="img" aria-label="Mini excavator on a residential lot" style="left:54px;top:316px;width:97px;height:66px;background:linear-gradient(160deg,#8fb0d6,#9aa070 55%,#6e7a3e)"></div>
  <div class="photo" role="img" aria-label="Excavator with trailer in a driveway" style="left:72px;top:388px;width:79px;height:66px;background:linear-gradient(160deg,#6f8fb5,#8a8a55 50%,#7d6a48)"></div>
  <div class="photo" role="img" aria-label="Excavator digging a trench beside trees" style="left:154px;top:304px;width:97px;height:157px;background:linear-gradient(170deg,#7aa0d0,#6f8a4a 35%,#9a8a6a 65%,#b7a890)"></div>
  <svg class="abs" style="left:133px;top:361px" width="42" height="42" viewBox="0 0 42 42"><circle cx="21" cy="21" r="20" fill="var(--lime)" stroke="#fff" stroke-width="1.5"/><path d="M13 20h3v9h-3zM17 20l3-6c1.5 0 2 1 1.8 2.2L21.3 19H26c1 0 1.7.9 1.4 1.9l-1.6 6.2c-.2.9-1 1.5-1.9 1.5H17z" fill="#111"/><circle cx="27" cy="15" r="4" fill="#111"/><path d="M25.2 15l1.3 1.3 2.3-2.6" stroke="var(--lime)" stroke-width=".9" fill="none"/></svg>

  <div class="abs display" style="left:269px;top:313px;font-size:3.2px;font-weight:700;display:flex;align-items:center;gap:3px"><span style="display:block;width:8px;height:5px;background:var(--lime)"></span>About Us<span style="display:block;width:104px;height:.6px;background:var(--lime)"></span></div>
  <div class="abs display" style="left:269px;top:326px;font-size:11px;line-height:16px">Building Perth's<br><span class="lime-text">Foundations</span></div>
  <p class="body-copy" style="left:269px;top:364px;width:156px;font-size:4.2px;line-height:7.2px">Gullwind Stonecut Earthworks is a Perth-based excavation company dedicated to delivering exceptional earthworks solutions. From residential projects to commercial developments, we bring the expertise and equipment needed to get the job done right.</p>
  <p class="body-copy" style="left:269px;top:400px;width:156px;font-size:4.2px;line-height:7.2px">Our commitment to safety, quality, and customer satisfaction sets us apart. We work closely with builders, developers, and homeowners across the Perth metropolitan area to ensure every project meets the highest standards.</p>
  <div class="btn btn--lime" style="left:269px;top:438px;width:51px;height:14px">Learn More <span>↗</span></div>

  <!-- SERVICES -->
  <div class="eyebrow" style="top:539px"><span>What We Do Us</span></div>
  <div class="heading" style="top:551px">Our <span class="lime-text">Services</span></div>

  <div class="service" role="img" aria-label="Excavated foundation pit in warm light" style="left:55px;background:linear-gradient(180deg,#6a4a22,#3a2a14 55%,#111 100%)">
    <h3 class="lime-text">Site<br>Preparation</h3>
    <svg class="abs" style="left:98px;top:100px" width="12" height="12" viewBox="0 0 12 12"><circle cx="6" cy="6" r="6" fill="var(--lime)"/><path d="M4 8l4-4M5 4h3v3" stroke="#111" stroke-width=".8" fill="none"/></svg>
    <p>Complete site clearing, leveling, and preparation for residential and commercial construction projects.</p>
  </div>
  <div class="service" role="img" aria-label="Deep red-soil trench with drainage pipes" style="left:180px;background:linear-gradient(180deg,#c0653a,#9a4a2a 55%,#2a1a12 100%)">
    <h3 style="color:#fff">Trenching &amp;<br>Drainage</h3>
    <p>Precision trenching for utilities, stormwater drainage, and sewer systems with minimal site disruption.</p>
  </div>
  <div class="service" role="img" aria-label="Yellow excavator demolishing a building" style="left:305px;background:linear-gradient(180deg,#9aa0a8,#6a6a6a 45%,#2a2a2a 100%)">
    <h3 style="color:#fff">Demolition</h3>
    <p style="top:110px">Safe and efficient demolition services for structures, concrete, and site obstacles.</p>
  </div>

  <div class="tag" style="left:55px;top:740px">Rock Breaking</div>
  <div class="tag" style="left:148px;top:740px">Pool Excavation</div>
  <div class="tag" style="left:241px;top:740px">Land Clearing</div>
  <div class="tag" style="left:334px;top:740px">Retaining Walls</div>
  <div class="tag" style="left:55px;top:759px">Driveway Preparation</div>
  <div class="tag" style="left:148px;top:759px">Bobcat Services</div>
  <div class="tag" style="left:241px;top:759px">Soil Removal</div>
  <div class="tag" style="left:334px;top:759px">Grading &amp; Leveling</div>

  <!-- PROJECTS -->
  <div class="band band--mist" style="top:816px;height:365px"></div>
  <div class="eyebrow" style="top:858px"><span>Portfolio</span></div>
  <div class="heading" style="top:870px">Some of Our <span class="lime-text">Projects</span></div>
  <div class="photo" role="img" aria-label="Narrow trench cut through brown soil" style="left:91px;top:903px;width:111px;height:85px;background:linear-gradient(180deg,#a0663c,#7a4a2a 60%,#5a3a22)"></div>
  <div class="photo" role="img" aria-label="Dozer clearing land with hills behind" style="left:208px;top:903px;width:119px;height:85px;background:linear-gradient(180deg,#c8d4de,#b8c6d0 35%,#4d6a4a 50%,#a0664a 75%,#8a5a3e)"></div>
  <div class="photo" role="img" aria-label="Excavator on a construction site" style="left:333px;top:903px;width:73px;height:85px;background:linear-gradient(180deg,#8fb4dc,#c0d4e4 45%,#b07a4a 70%,#8a5a3a)"></div>
  <div class="photo" role="img" aria-label="Machinery beside a flooded site at dusk" style="left:55px;top:994px;width:73px;height:85px;background:linear-gradient(180deg,#c8ccd0,#9aa0a0 50%,#b88a7a 75%,#a07060)"></div>
  <div class="photo" role="img" aria-label="Bulldozer working in a forest clearing" style="left:134px;top:994px;width:141px;height:112px;background:linear-gradient(180deg,#3a4a30,#5a5a3a 45%,#9a7040 70%,#8a5a3a)"></div>
  <div class="photo" role="img" aria-label="Workers and excavator on an urban site" style="left:281px;top:994px;width:109px;height:85px;background:linear-gradient(180deg,#a8c4e0,#c8c0b0 45%,#8a6a4a 75%,#6a4a32)"></div>
  <div class="btn btn--lime" style="left:205px;top:1125px;width:68px;height:13px">View All Projects <span>↗</span></div>

  <!-- TRUST -->
  <div class="eyebrow" style="top:1223px"><span>Why Choose Us</span></div>
  <div class="heading" style="top:1235px">Building <span class="lime-text">Trust</span></div>

  <div class="trust" style="left:55px">
    <svg width="17" height="17" viewBox="0 0 17 17" fill="none" stroke="var(--lime)" stroke-width=".8"><rect x="4" y="2" width="9" height="13"/><path d="M8.5 5l2 1v2c0 1.5-1 2.5-2 3-1-.5-2-1.5-2-3V6z"/></svg>
    <h4 style="top:42px">Fully Insured</h4>
    <p style="top:53px">Complete public liability and professional indemnity coverage for your peace of mind.</p>
  </div>
  <div class="trust" style="left:148px">
    <svg width="17" height="17" viewBox="0 0 17 17" fill="none" stroke="var(--lime)" stroke-width=".8"><circle cx="7" cy="5" r="2.5"/><path d="M4 5h6M2.5 15c0-3 2-5 4.5-5s4.5 2 4.5 5"/><circle cx="13" cy="12" r="2.5"/><path d="M13 10.8v1.3l.8.6"/></svg>
    <h4 style="top:42px">On-Time Delivery</h4>
    <p style="top:53px">We respect your timeline and deliver projects on schedule, every time.</p>
  </div>
  <div class="trust" style="left:242px">
    <svg width="17" height="17" viewBox="0 0 17 17" fill="none" stroke="var(--lime)" stroke-width=".8"><circle cx="8.5" cy="7" r="5"/><circle cx="8.5" cy="7" r="2.5"/><path d="M6 11.5l-1.5 4 2-1 1 1.5M11 11.5l1.5 4-2-1-1 1.5"/></svg>
    <h4 style="top:42px">Quality First</h4>
    <p style="top:53px">Precision workmanship and attention to detail on every job, big or small.</p>
  </div>
  <div class="trust" style="left:336px">
    <svg width="17" height="17" viewBox="0 0 17 17" fill="none" stroke="var(--lime)" stroke-width=".8" style="top:9px"><rect x="1.5" y="3" width="14" height="10"/><circle cx="5" cy="7" r="1.5"/><path d="M3 11c0-1.2 1-2 2-2s2 .8 2 2M9 6h5M9 8h5M9 10h3"/></svg>
    <h4 style="top:34px">Licensed<br>Operators</h4>
    <p style="top:53px">Experienced and certified operators with extensive industry knowledge.</p>
  </div>

  <!-- TESTIMONIALS -->
  <div class="band band--mist" style="top:1393px;height:235px"></div>
  <div class="eyebrow" style="top:1427px"><span>Testimonials</span></div>
  <div class="heading" style="top:1438px">What Our Clients<br><span class="lime-text">Say About Us</span></div>

  <div class="review" style="left:55px"><div class="stars">★★★★★</div><blockquote>"Gullwind Stonecut delivered exceptional site prep for our housing development. Professional, on time, and the quality of work was outstanding. Highly recommend for any earthworks project."</blockquote><div class="rule"></div><div class="who">Liam Harcourt<small>Builder, Harcourt Building Co.</small></div></div>
  <div class="review" style="left:180px"><div class="stars">★★★★★</div><blockquote>"We've used Gullwind Stonecut on multiple projects across Perth. Their attention to detail and reliability is unmatched. The team goes above and beyond every time."</blockquote><div class="rule"></div><div class="who">Nora Pellam<small>Property Developer</small></div></div>
  <div class="review" style="left:305px"><div class="stars">★★★★★</div><blockquote>"Needed trenching work for my new pool installation. The crew was friendly, efficient, and left the site spotless. Fair pricing and great communication throughout."</blockquote><div class="rule"></div><div class="who">Owen Ridley<small>Homeowner, Joondalup</small></div></div>

  <div class="abs" style="left:226px;top:1592px;width:10px;height:1.4px;background:#222"></div>
  <div class="abs" style="left:240px;top:1592px;width:1.4px;height:1.4px;background:#999;border-radius:50%"></div>
  <div class="abs" style="left:245px;top:1592px;width:1.4px;height:1.4px;background:#999;border-radius:50%"></div>
  <div class="abs" style="left:250px;top:1592px;width:1.4px;height:1.4px;background:#999;border-radius:50%"></div>

  <!-- CTA -->
  <div class="heading" style="top:1655px">Ready to <span class="lime-text">Get Started ?</span></div>
  <p class="body-copy" style="left:0;width:477px;top:1678px;text-align:center;font-size:4.2px;line-height:7.6px">Whether you need site preparation, trenching, or demolition services, we're here to help.<br>Get in touch for a free, no-obligation quote on your next earthworks project.</p>
  <div class="btn btn--dark" style="left:191px;top:1704px;width:43px;height:13px">Get a Quote</div>
  <div class="btn btn--lime" style="left:239px;top:1704px;width:47px;height:13px">
    <svg width="6" height="6" viewBox="0 0 10 10"><circle cx="5" cy="5" r="4.4" fill="none" stroke="#111" stroke-width=".8"/><path d="M3.3 2.8l1 1-.5.7c.4.8 1 1.4 1.8 1.8l.7-.5 1 1-.7.8c-1.9-.3-3.3-1.7-3.6-3.6z" fill="#111"/></svg>Call Now</div>

  <!-- FOOTER -->
  <div class="footer">
    <div class="photo" role="img" aria-label="Silhouettes of excavators, a loader and trucks along the skyline" style="left:0;top:0;width:477px;height:70px;background:linear-gradient(180deg,#ffffff 0%,#ffffff 20%,#1a1a1a 70%,var(--night))"></div>
  </div>
  <div class="brand" style="left:70px;top:1847px;flex-direction:column;color:#fff;text-align:center;gap:4px"><i></i><span>Gullwind Stonecut<br>Earthworks</span></div>
  <div class="social" style="left:72px"></div>
  <div class="social" style="left:86px"></div>
  <div class="social" style="left:100px"></div>
  <div class="social" style="left:114px"></div>

  <div class="footer" style="background:none;top:1745px">
    <h5 style="left:146px;top:88px">Quick Links</h5>
    <ul style="left:146px;top:98px"><li>Home</li><li>About Us</li><li>Services</li><li>Projects</li><li>Testimonials</li><li>Contact</li></ul>
    <h5 style="left:213px;top:88px">Services</h5>
    <ul style="left:213px;top:98px"><li>Site Preparation</li><li>Trenching and Drainage</li><li>Demolition</li><li>Land Clearing</li><li>Bobcat Services</li><li>Grading and Leveling</li></ul>
    <ul style="left:281px;top:98px"><li>Pool Excavation</li><li>Rock Breaking</li><li>Driveway Preparation</li><li>Soil Removal</li><li>Retaining Walls</li></ul>
    <h5 style="left:348px;top:88px">Contact Us</h5>
    <ul style="left:348px;top:99px;line-height:12.5px;color:#ddd">
      <li><span style="display:inline-block;width:6px;height:6px;border:.6px solid var(--lime);border-radius:50%;vertical-align:middle;margin-right:3px"></span>+61 400 555 018</li>
      <li><span style="display:inline-block;width:6px;height:6px;border:.6px solid var(--lime);border-radius:50%;vertical-align:middle;margin-right:3px"></span>hello@gullwindstonecut.example</li>
      <li><span style="display:inline-block;width:6px;height:6px;border:.6px solid var(--lime);border-radius:50%;vertical-align:middle;margin-right:3px"></span>Perth, WA, Australia</li>
    </ul>
    <div class="abs" style="left:0;top:175px;width:477px;text-align:center;font-size:3.2px;color:#999">© 2026 Gullwind Stonecut Earthworks. All rights reserved.</div>
  </div>

</div>
</body>
</html>
```